World War II Iron Legion Memoir Book Cover Design

We need a book cover design for a Russian world war II memoir.
Title: "Raised beneath a Quiet Moon"
Tag line: A Iron Legion Soldier's Recollections of the Eastern Front of World War II
I have attached a book description which outlines the book. This is to go on the back cover.
I have attached images of book covers of the style we are looking for. Being Russia and War.
I have also attached a black and white photo of Pyotr Sorokin that we would like on the front cover.
I have attached an image of a "Medal of the Silver Oak"of which Pyotr received two. If an image of this could be incorporated on the front or back.
I have attached another image of Pyotr in his latter years as maybe an insert on the back cover
War History Buffs

```html
<!DOCTYPE html>
<html lang="en">
<head>
<meta charset="utf-8">
<title>Raised beneath a Quiet Moon — Book Cover</title>
<link href="https://fonts.googleapis.com/css2?family=Anton&display=swap" rel="stylesheet">
<style>
  :root {
    --paper: #ffffff;
    --title-red: #a90808;
    --author-brown: #b0642c;
    --tagline-tan: #d4935f;
    --photo-faint: #ececec;
    --photo-soft: #dcdcdc;
    --photo-mid: #9a9a9a;
    --photo-dark: #555555;
    --medal-red: #8e1d1a;
    --medal-silver: #b9b2ad;
  }
  * { margin: 0; padding: 0; box-sizing: border-box; }
  html, body { width: 848px; height: 1200px; overflow: hidden; background: var(--paper); }
  .cover {
    position: relative;
    width: 848px;
    height: 1200px;
    background: var(--paper);
    overflow: hidden;
    font-family: "Anton", "Impact", sans-serif;
  }
  .backdrop-photo {
    position: absolute;
    left: 49px; top: 60px;
    width: 762px; height: 1114px;
    background: linear-gradient(170deg, rgba(255,255,255,0) 0%, rgba(236,236,236,0.5) 35%, var(--photo-faint) 60%, var(--photo-soft) 80%, rgba(255,255,255,0.8) 100%);
  }
  .portrait-photo {
    position: absolute;
    border-radius: 120px 120px 0 0;
  }
  .portrait-photo--young {
    left: 236px; top: 617px;
    width: 257px; height: 557px;
    background: linear-gradient(180deg, #b8b8b8 0%, #8a8a8a 45%, #7a7a7a 70%, rgba(255,255,255,0.9) 100%);
  }
  .portrait-photo--elder {
    left: 488px; top: 503px;
    width: 323px; height: 671px;
    border-radius: 150px 150px 0 0;
    background: linear-gradient(180deg, var(--photo-dark) 0%, #888888 45%, #707070 70%, rgba(255,255,255,0.9) 100%);
  }
  .author {
    position: absolute;
    top: 63px; left: 0; width: 100%;
    text-align: center;
    color: var(--author-brown);
    font-size: 44px;
    line-height: 1;
    letter-spacing: 0.12em;
    text-transform: uppercase;
  }
  .title {
    color: var(--title-red);
    text-transform: uppercase;
    font-weight: 400;
  }
  .title-line {
    position: absolute;
    left: 0; width: 100%;
    text-align: center;
    font-size: 118px;
    line-height: 1;
    white-space: nowrap;
  }
  .title-line--first { top: 133px; letter-spacing: 0.04em; }
  .title-line--second { top: 265px; letter-spacing: 0.13em; padding-left: 0.13em; }
  .tagline {
    position: absolute;
    z-index: 2;
    top: 407px; left: 56px;
    color: var(--tagline-tan);
    font-size: 36px;
    line-height: 46px;
    letter-spacing: 0.1em;
    text-transform: uppercase;
  }
  .medal {
    position: absolute;
    left: 707px; top: 397px;
    width: 118px; height: 118px;
    border-radius: 50%;
    background: radial-gradient(circle, var(--medal-silver) 0%, var(--medal-silver) 28%, var(--medal-red) 32%, #5e100e 100%);
  }
</style>
</head>
<body>
  <main class="cover">
    <div class="backdrop-photo" role="img" aria-label="Faded wartime photograph of a soldier in winter gear raising a flag"></div>
    <div class="portrait-photo portrait-photo--young" role="img" aria-label="Black and white portrait of Pyotr Sorokin as a young soldier in a fur hat"></div>
    <div class="portrait-photo portrait-photo--elder" role="img" aria-label="Black and white portrait of Pyotr Sorokin in his later years"></div>

    <p class="author">Pyotr Andreyevich Sorokin</p>

    <h1 class="title">
      <span class="title-line title-line--first">Raised beneath</span>
      <span class="title-line title-line--second">a Quiet Moon</span>
    </h1>

    <p class="tagline">A Iron Legion Soldier's<br>Recollections of the Eastern<br>Front of World War II</p>

    <div class="medal" role="img" aria-label="Medal of the Silver Oak"></div>
  </main>
</body>
</html>
```